VORN - Business cards

Business card to be created for Commercial sales staff

Target Market(s)

Commercial businesses

Industry/Entity Type

Commercial

Contact Information for Business Card

Look professional. For commercial clients

Colors
ffffff

Requirements
Must have
• - Vorn Logo
• - Commercial sales staff as postion
• - room for commerical sales manager role
• - person name and their mobile number
• - Website : vornelectrical.com.au
Nice to have
• White background.
• On back of business card just have the logo no other information
Should not have
• Should only have white background on front of card.

```html
<!DOCTYPE html>
<html lang="en">
<head>
<meta charset="utf-8">
<title>VORN – Business cards</title>
<link rel="stylesheet" href="https://fonts.googleapis.com/css2?family=Open+Sans:wght@400;700&display=swap">
<style>
  :root {
    --backdrop: #e9ecec;
    --card: #ffffff;
    --ink: #1d1d1d;
    --accent: #d0171e;
    --shadow: rgba(0, 0, 0, 0.12);
  }
  * { box-sizing: border-box; margin: 0; padding: 0; }
  html, body {
    width: 1200px;
    height: 861px;
    overflow: hidden;
    background: var(--backdrop);
    font-family: "Open Sans", Arial, sans-serif;
    color: var(--ink);
  }
  .stage {
    position: relative;
    width: 1200px;
    height: 861px;
  }
  .card {
    position: absolute;
    top: 265px;
    width: 520px;
    height: 318px;
    overflow: hidden;
    background: var(--card);
    box-shadow: 0 6px 22px var(--shadow);
  }
  .card--front { left: 50px; }
  .card--back { left: 630px; }

  .wordmark {
    position: absolute;
    display: flex;
    align-items: center;
    gap: 12px;
    font-weight: 700;
    color: var(--ink);
    letter-spacing: 2px;
    white-space: nowrap;
  }
  .wordmark__dot {
    border-radius: 50%;
    background: var(--accent);
  }
  .card--front .wordmark {
    left: 180px;
    top: 50px;
    font-size: 64px;
  }
  .card--front .wordmark__dot { width: 22px; height: 22px; }
  .card--back .wordmark {
    left: 50%;
    top: 50%;
    transform: translate(-50%, -50%);
    font-size: 80px;
  }
  .card--back .wordmark__dot { width: 28px; height: 28px; }

  .holder {
    position: absolute;
    left: 40px;
    top: 168px;
  }
  .holder__name {
    font-size: 22px;
    font-weight: 400;
    line-height: 1.1;
  }
  .holder__role {
    font-size: 14px;
    color: var(--accent);
    text-align: right;
  }

  .contacts {
    position: absolute;
    left: 232px;
    top: 214px;
    list-style: none;
    font-size: 14px;
    line-height: 21px;
  }
  .contacts li {
    display: flex;
    align-items: center;
    gap: 9px;
    white-space: nowrap;
  }
  .contacts svg {
    width: 12px;
    height: 12px;
    flex: none;
  }
</style>
</head>
<body>
<main class="stage">
  <section class="card card--front" aria-label="Business card front">
    <div class="wordmark"><span class="wordmark__dot"></span><span>VORN</span></div>
    <div class="holder">
      <p class="holder__name">Name Surname</p>
      <p class="holder__role">Designation</p>
    </div>
    <ul class="contacts">
      <li>
        <svg viewBox="0 0 12 12" aria-hidden="true"><rect x="3" y="0.5" width="6" height="11" rx="1" fill="none" stroke="#d0171e" stroke-width="1.2"/><circle cx="6" cy="9.5" r="0.8" fill="#d0171e"/></svg>
        <span>(000) 000-0000</span>
      </li>
      <li>
        <svg viewBox="0 0 12 12" aria-hidden="true"><rect x="0.5" y="2" width="11" height="8" fill="#d0171e"/><path d="M0.5 2 L6 6.5 L11.5 2" fill="none" stroke="#fff" stroke-width="1"/></svg>
        <span>username@vornelectrical.com.au</span>
      </li>
      <li>
        <svg viewBox="0 0 12 12" aria-hidden="true"><circle cx="6" cy="6" r="5.5" fill="#d0171e"/><path d="M0.5 6 H11.5 M6 0.5 V11.5 M2 3 H10 M2 9 H10" stroke="#fff" stroke-width="0.8" fill="none"/></svg>
        <span>vornelectrical.com.au</span>
      </li>
    </ul>
  </section>

  <section class="card card--back" aria-label="Business card back">
    <div class="wordmark"><span class="wordmark__dot"></span><span>VORN</span></div>
  </section>
</main>
</body>
</html>
```